Tending the Hidden Garden; A Map Toward Calm, Purpose & Belonging

I need a book cover, for the above book title. This is a journey of the heart to know the heart of God. I think on the text, Simple (see below graphic)
Black Lettering for Tending.....Garden
Gold lettering for God
Either gold or black for the subtitle; A Map Toward Calm, Purpose, & Belonging
I would like the below graphic idea only no photograph of a person,
and White background instead of black
Simple Font, like below graphic, but open to suggestions

not age specific, Every person has been given a heart to know God, we are taking the mystery out the process to understand God is Father, loving gracious, ever present, etc. If we know His heart, we realize He's not at a distance, He is there, an ever present help

Security

• Title: Tending the Hidden Garden; A Map Toward Calm, Purpose, & Belonging
• My name, Rob Fenwick
• See Below Graphic

```html
<!DOCTYPE html>
<html lang="en">
<head>
<meta charset="utf-8">
<title>Tending the Hidden Garden — Rob Fenwick</title>
<link rel="stylesheet" href="https://fonts.googleapis.com/css2?family=Anton&family=Oswald:wght@500;600&family=Russo+One&display=swap">
<style>
  :root {
    --paper: #ffffff;
    --mist: #eef2f7;
    --mist-edge: #dfe6ef;
    --ray: rgba(170, 190, 215, 0.35);
    --gold-light: #fff6c8;
    --gold: #e9c032;
    --gold-deep: #8a5e12;
    --gold-edge: #6e430a;
    --ink: #0b1a20;
    --ink-teal: #1f4650;
    --ink-top: #2b5a66;
    --glow: #9fe6ff;
  }
  * { margin: 0; padding: 0; box-sizing: border-box; }
  html, body { width: 928px; height: 1200px; overflow: hidden; background: var(--paper); }
  .cover {
    position: relative;
    width: 928px;
    height: 1200px;
    overflow: hidden;
    background: radial-gradient(ellipse 70% 60% at 50% 45%, var(--paper) 0%, var(--paper) 55%, var(--mist) 85%, var(--mist-edge) 100%);
  }
  .cover__art { position: absolute; inset: 0; width: 928px; height: 1200px; }
  .title-dark { font-family: "Russo One", sans-serif; }
  .title-gold { font-family: "Anton", sans-serif; }
  .author, .subtitle { font-family: "Oswald", sans-serif; }
  .author { font-weight: 600; }
  .subtitle { font-weight: 500; }
</style>
</head>
<body>
<main class="cover">
  <svg class="cover__art" viewBox="0 0 928 1200" aria-labelledby="book-title">
    <title id="book-title">Tending the Hidden Garden: A Map Toward Calm, Purpose, &amp; Belonging, by Rob Fenwick</title>
    <defs>
      <linearGradient id="ink-fill" x1="0" y1="0" x2="0" y2="1">
        <stop offset="0" stop-color="var(--ink-top)"/>
        <stop offset="0.45" stop-color="var(--ink)"/>
        <stop offset="0.6" stop-color="var(--ink-teal)"/>
        <stop offset="1" stop-color="var(--ink)"/>
      </linearGradient>
      <linearGradient id="gold-fill" x1="0" y1="0" x2="0" y2="1">
        <stop offset="0" stop-color="#fffdf0"/>
        <stop offset="0.2" stop-color="var(--gold-light)"/>
        <stop offset="0.42" stop-color="var(--gold)"/>
        <stop offset="0.55" stop-color="var(--gold-deep)"/>
        <stop offset="0.68" stop-color="var(--gold)"/>
        <stop offset="0.85" stop-color="var(--gold-light)"/>
        <stop offset="1" stop-color="var(--gold)"/>
      </linearGradient>
      <filter id="cyan-glow" x="-10%" y="-30%" width="120%" height="160%">
        <feGaussianBlur in="SourceAlpha" stdDeviation="5" result="blur"/>
        <feFlood flood-color="#9fe6ff" flood-opacity="0.9"/>
        <feComposite in2="blur" operator="in" result="glow"/>
        <feMerge><feMergeNode in="glow"/><feMergeNode in="SourceGraphic"/></feMerge>
      </filter>
    </defs>

    <g class="light-rays" stroke="var(--ray)" stroke-width="1.5" aria-hidden="true">
      <line x1="464" y1="520" x2="0" y2="40"/>
      <line x1="464" y1="520" x2="928" y2="40"/>
      <line x1="464" y1="520" x2="0" y2="330"/>
      <line x1="464" y1="520" x2="928" y2="300"/>
      <line x1="464" y1="520" x2="0" y2="760"/>
      <line x1="464" y1="520" x2="928" y2="780"/>
      <line x1="464" y1="520" x2="250" y2="0"/>
      <line x1="464" y1="520" x2="690" y2="0"/>
    </g>

    <text class="author" x="464" y="192" font-size="56" text-anchor="middle" letter-spacing="20"
          fill="url(#gold-fill)" stroke="var(--gold-edge)" stroke-width="1">ROB  FENWICK</text>

    <text class="title-dark" x="90" y="480" font-size="150" textLength="738" lengthAdjust="spacingAndGlyphs"
          fill="url(#ink-fill)" stroke="#e6fbff" stroke-width="1.5" filter="url(#cyan-glow)">TENDING THE</text>

    <text class="title-gold" x="80" y="846" font-size="404" textLength="758" lengthAdjust="spacingAndGlyphs"
          fill="url(#gold-fill)" stroke="var(--gold-edge)" stroke-width="3">HIDDEN</text>

    <text class="title-dark" x="78" y="978" font-size="168" textLength="756" lengthAdjust="spacingAndGlyphs"
          fill="url(#ink-fill)" stroke="#e6fbff" stroke-width="1.5" filter="url(#cyan-glow)">GARDEN</text>

    <text class="subtitle" x="72" y="1140" font-size="52" textLength="756" lengthAdjust="spacingAndGlyphs"
          fill="url(#gold-fill)" stroke="var(--gold-edge)" stroke-width="1">A MAP TOWARD CALM, PURPOSE, &amp; BELONGING</text>
  </svg>
</main>
</body>
</html>
```